Business card with professional look

I would like a creative yet professional looking business card for our business. We sell broadcast TV related security products for mobile phones, set top boxes, and tablets. Our customers are international. We have a logo we like and I would like to possibly add some color to the business card but keep it professional looking.

Target Market(s)

Professionals in the TV, cable, ans Satellite industries

Industry/Entity Type

Cable Tv

Contact Information for Business Card

Name Ned Vastermill, title CEO, Address 8130 Harborline Court, Suite 400, Del Arvo, CA 91584 USA, phone numbers m:+1.619.284.7302 o:+1.855.672.9140, email, logo

Font styles to use
Other font styles liked:
• Open to any font that looks good with logo

Requirements
Must have
• professional look with colors coordinated with logo colors. would like to add one or two different colors as well as some form of background color

```html
<!DOCTYPE html>
<html lang="en">
<head>
<meta charset="utf-8">
<title>VaultView Business Card</title>
<link rel="stylesheet" href="https://fonts.googleapis.com/css2?family=Montserrat:wght@700&family=Questrial&display=swap">
<style>
  :root {
    --page: #2e2f31;
    --blue-deep: #0a5fb4;
    --blue-bright: #12a3e0;
    --blue-ink: #0b6cc0;
    --grey-band: #5b5c5f;
    --grey-text: #5a5a5c;
    --paper: #f7f7f7;
    --white: #ffffff;
  }
  * { margin: 0; padding: 0; box-sizing: border-box; }
  html, body { width: 1200px; height: 900px; overflow: hidden; }
  body {
    background: var(--page);
    font-family: "Questrial", sans-serif;
    display: flex;
    flex-direction: column;
    align-items: center;
    justify-content: center;
    gap: 60px;
  }
  .card {
    position: relative;
    width: 630px;
    height: 360px;
    overflow: hidden;
    border-radius: 3px;
    box-shadow: 0 14px 30px rgba(0,0,0,0.45);
  }

  /* Back side */
  .card-back {
    background: linear-gradient(135deg, var(--blue-deep) 0%, var(--blue-bright) 100%);
  }
  .card-back .grey-band {
    position: absolute; left: 0; right: 0; bottom: 0; height: 34px;
    background: var(--grey-band);
  }
  .card-back .brand {
    position: absolute; left: 0; right: 0; top: 120px;
    display: flex; align-items: center; justify-content: center; gap: 12px;
  }
  .brand-name {
    font-family: "Montserrat", sans-serif;
    font-weight: 700;
    letter-spacing: -1px;
  }
  .card-back .brand-name { font-size: 54px; color: var(--white); }
  .card-back .brand-square {
    width: 26px; height: 26px; background: var(--white); border-radius: 4px;
  }
  .card-back .web {
    position: absolute; left: 0; right: 0; top: 222px;
    text-align: center; color: var(--white); font-size: 15px; letter-spacing: 0.5px;
  }

  /* Front side */
  .card-front { background: var(--paper); }
  .card-front .blue-panel {
    position: absolute; left: 0; right: 0; top: 196px; bottom: 34px;
    background: linear-gradient(120deg, var(--blue-deep) 0%, var(--blue-bright) 100%);
  }
  .card-front .notch {
    position: absolute; left: 52px; top: -9px;
    width: 0; height: 0;
    border-left: 10px solid transparent;
    border-right: 10px solid transparent;
    border-bottom: 10px solid var(--blue-deep);
  }
  .card-front .faint-mark {
    position: absolute; left: 340px; top: 10px;
    width: 110px; height: 90px; border-radius: 14px;
    background: rgba(255,255,255,0.08);
  }
  .card-front .grey-band {
    position: absolute; left: 0; right: 0; bottom: 0; height: 34px;
    background: var(--grey-band);
  }
  .card-front .brand {
    position: absolute; right: 40px; top: 58px;
    display: flex; align-items: center; gap: 10px;
  }
  .card-front .brand-name { font-size: 44px; color: var(--grey-text); }
  .card-front .brand-square {
    width: 22px; height: 22px; background: var(--blue-ink); border-radius: 4px;
  }
  .holder {
    position: absolute; left: 40px; top: 132px;
  }
  .holder-name {
    font-family: "Montserrat", sans-serif; font-weight: 700;
    font-size: 21px; color: var(--blue-ink); text-transform: uppercase; letter-spacing: 0.5px;
  }
  .holder-title { font-size: 17px; color: var(--grey-text); margin-top: 2px; }
  .contacts {
    position: absolute; left: 40px; top: 20px;
    list-style: none;
  }
  .contacts li {
    display: flex; align-items: center; gap: 10px;
    color: var(--white); font-size: 14px; height: 22px; letter-spacing: 0.3px;
  }
  .contacts svg { width: 16px; height: 16px; flex: none; }
  .address {
    position: absolute; right: 34px; top: 22px;
    text-align: right; color: var(--white); font-size: 14px; line-height: 21px; font-style: normal;
  }
</style>
</head>
<body>
  <section class="card card-back">
    <div class="brand">
      <span class="brand-name">VaultView</span>
      <span class="brand-square"></span>
    </div>
    <p class="web">www.vaultview.com</p>
    <div class="grey-band"></div>
  </section>

  <section class="card card-front">
    <div class="brand">
      <span class="brand-name">VaultView</span>
      <span class="brand-square"></span>
    </div>
    <div class="holder">
      <h1 class="holder-name">Ned Vastermill</h1>
      <p class="holder-title">CEO</p>
    </div>
    <div class="blue-panel">
      <span class="notch"></span>
      <span class="faint-mark"></span>
      <ul class="contacts">
        <li>
          <svg viewBox="0 0 16 16"><rect width="16" height="16" rx="3" fill="rgba(255,255,255,0.85)"/><rect x="5" y="3" width="6" height="10" rx="1" fill="none" stroke="#0a5fb4" stroke-width="1.3"/></svg>
          +1.619.284.7302
        </li>
        <li>
          <svg viewBox="0 0 16 16"><rect width="16" height="16" rx="3" fill="rgba(255,255,255,0.85)"/><path d="M5 3.5l2 2-1 1.2c.6 1.3 1.6 2.3 2.9 2.9l1.2-1 2 2-1.3 1.6C7.5 12 4 8.5 3.8 5.1z" fill="#0a5fb4"/></svg>
          +1.855.672.9140
        </li>
        <li>
          <svg viewBox="0 0 16 16"><rect width="16" height="16" rx="3" fill="rgba(255,255,255,0.85)"/><rect x="3" y="4.5" width="10" height="7" fill="none" stroke="#0a5fb4" stroke-width="1.3"/><path d="M3 4.5l5 4 5-4" fill="none" stroke="#0a5fb4" stroke-width="1.3"/></svg>
          info@vaultview.com
        </li>
        <li>
          <svg viewBox="0 0 16 16"><rect width="16" height="16" rx="3" fill="rgba(255,255,255,0.85)"/><circle cx="8" cy="8" r="4.8" fill="none" stroke="#0a5fb4" stroke-width="1.2"/><ellipse cx="8" cy="8" rx="2" ry="4.8" fill="none" stroke="#0a5fb4" stroke-width="1"/><path d="M3.2 8h9.6" stroke="#0a5fb4" stroke-width="1"/></svg>
          www.vaultview.com
        </li>
      </ul>
      <address class="address">
        8130 Harborline Court,<br>
        Suite 400, Del Arvo,<br>
        CA 91584 USA
      </address>
    </div>
    <div class="grey-band"></div>
  </section>
</body>
</html>
```